Business Card for Inovative Flexible Packaging Company

Create a business card that is both simple and stricking at the same time.
Preferably only one color (orange) or two colors (black and orange).
Information to print:
Torvalo, Lda
[T] 22 418 6093
[M] 91 326 7041
[F] 22 418 6135
[@] torvalo.ac@correiomx.com
SEDE & ARMAZÉM
Rua Das Figueiras do Monte, 312
Valmoura
4730-256 Valmoura - Alvarenga
PORTUGAL
Reason: A lot of the ideas are obvious. I want something different. Inovative. dare to do something eye catching with style.
Business Consumers. Packaging Designers.
Business

```html
<!DOCTYPE html>
<html lang="pt">
<head>
<meta charset="utf-8">
<title>Torvalo business card</title>
<link rel="stylesheet" href="https://fonts.googleapis.com/css2?family=Montserrat:wght@600;700&family=Arimo:wght@400;700&display=swap">
<style>
  :root {
    --backdrop: #1c1c1c;
    --card: #ffffff;
    --orange: #f26a1b;
    --orange-soft: #f8a46c;
    --ink: #161616;
    --grey: #3c3c3c;
  }
  * { box-sizing: border-box; margin: 0; padding: 0; }
  html, body { width: 1200px; height: 873px; overflow: hidden; }
  body {
    background: var(--backdrop);
    display: flex;
    align-items: center;
    justify-content: center;
    gap: 60px;
    font-family: "Arimo", Arial, sans-serif;
  }
  .card {
    width: 520px;
    height: 315px;
    background: var(--card);
    position: relative;
    overflow: hidden;
    box-shadow: 0 10px 30px rgba(0,0,0,.5);
  }
  /* front */
  .card-front { display: flex; align-items: center; justify-content: center; }
  .brand { display: flex; flex-direction: column; align-items: flex-start; }
  .brand-row { display: flex; align-items: center; gap: 14px; }
  .brand-square { width: 44px; height: 44px; background: var(--orange); }
  .brand-name {
    font-family: "Montserrat", Arial, sans-serif;
    font-weight: 700;
    font-size: 64px;
    line-height: 1;
    color: var(--orange);
    letter-spacing: -1px;
  }
  .brand-tagline {
    margin-top: 10px;
    margin-left: 58px;
    font-size: 11px;
    letter-spacing: 4.2px;
    color: var(--grey);
    text-transform: uppercase;
    white-space: nowrap;
  }
  /* back */
  .shard-field {
    position: absolute;
    left: 0; top: 0;
    width: 250px; height: 315px;
    background: linear-gradient(135deg, var(--orange-soft) 0%, #fbc79f 55%, var(--card) 100%);
  }
  .contact {
    position: absolute;
    left: 280px; top: 34px;
    right: 16px;
    color: var(--ink);
  }
  .contact-name { font-weight: 700; font-size: 17px; margin-bottom: 16px; }
  .contact-list { list-style: none; font-size: 11px; line-height: 1.45; }
  .contact-list li { display: flex; gap: 8px; align-items: flex-start; margin-bottom: 3px; }
  .contact-list svg { width: 11px; height: 11px; flex: none; margin-top: 2px; fill: var(--orange); }
  .address { display: block; }
</style>
</head>
<body>
  <section class="card card-front">
    <div class="brand">
      <div class="brand-row">
        <span class="brand-square"></span>
        <span class="brand-name">torvalo</span>
      </div>
      <p class="brand-tagline">Adaptive Wrapping</p>
    </div>
  </section>

  <section class="card card-back">
    <div class="shard-field" role="img" aria-label="Overlapping translucent orange geometric shards"></div>
    <div class="contact">
      <h1 class="contact-name">Torvalo, Lda</h1>
      <ul class="contact-list">
        <li><svg viewBox="0 0 12 12"><path d="M2 1l2.5 0 1 3-1.5 1a7 7 0 0 0 3 3l1-1.5 3 1V10a1 1 0 0 1-1 1A9 9 0 0 1 1 2a1 1 0 0 1 1-1z"/></svg>22 418 6093</li>
        <li><svg viewBox="0 0 12 12"><path d="M3 0h6a1 1 0 0 1 1 1v10a1 1 0 0 1-1 1H3a1 1 0 0 1-1-1V1a1 1 0 0 1 1-1zm0 1.5v8h6v-8z"/></svg>91 326 7041</li>
        <li><svg viewBox="0 0 12 12"><path d="M3 0h6v3h2a1 1 0 0 1 1 1v6H0V4a1 1 0 0 1 1-1h2zm1 1v2h4V1zM2 6v1h2V6zm0 2v1h2V8zm4-2h4v3H6z"/></svg>22 418 6135</li>
        <li><svg viewBox="0 0 12 12"><path d="M0 2h12v8H0zm1 1v.4l5 3.3 5-3.3V3zm0 1.6V9h10V4.6L6 8z"/></svg>torvalo.ac@correiomx.com</li>
        <li><svg viewBox="0 0 12 12"><path d="M6 0a4 4 0 0 1 4 4c0 3-4 8-4 8S2 7 2 4a4 4 0 0 1 4-4zm0 2.3a1.7 1.7 0 1 0 0 3.4 1.7 1.7 0 0 0 0-3.4z"/></svg>
          <span class="address">SEDE &amp; ARMAZÉM<br>Rua Das Figueiras do Monte, 312<br>Valmoura<br>4730-256 Valmoura - Alvarenga<br>PORTUGAL</span>
        </li>
      </ul>
    </div>
  </section>
</body>
</html>
```